A 3d printing services company "The Velvet Lattice" needs a clutter breaking business card design

The Velvet Lattice is a 3d design, animation and printing services company. We are in the B2B and B2C space. www.velvetlattice.com.sg
We have been in business for a year.
The logo is already done (the current file is attached).
We need a business card design which reflects the 3d printing and animations services of the company. A standard rectangular shape is not an option. The card can be die cut.
The card should have the colors of the logo and should have a high tech wow feel to it.
The front of the card should have my name, designation, cellphone email and website details. No need for an office address.
Name: Raghavan Kulkarni
Designation: Founder Director
Cellphone (65)91827345
email: raghavan@velvetlattice.com.sg
website: www.velvetlattice.com.sg
The back of the card should have the services we offer:
1. 3d Design and Modelling
2. 3d Animation
3. 3D Printing
The tag line is: "make your ideas real"
Am uploading the current business card files(back and front).
Target Market(s)
Business owners and C level managers in Marine, Healthcare industry
Industry/Entity Type
Printing
Contact Information for Business Card
Name: Raghavan Kulkarni
Cellphone (65)91827345
2. 3d Animation
3. 3D Printing

```html
<!DOCTYPE html>
<html lang="en">
<head>
<meta charset="utf-8">
<title>The Velvet Lattice — Business Card</title>
<link rel="stylesheet" href="https://fonts.googleapis.com/css2?family=Questrial&display=swap">
<style>
  :root {
    --page: #e9e9ec;
    --navy-deep: #050d2e;
    --navy: #0b1f5c;
    --blue: #2f63c9;
    --blue-light: #7aa2ea;
    --green: #7cc936;
    --grey-text: #6d6d72;
    --label: #ffffff;
    --paper: #ffffff;
  }
  * { margin: 0; padding: 0; box-sizing: border-box; }
  html, body { width: 1200px; height: 1000px; overflow: hidden; }
  body {
    background: var(--page);
    font-family: "Questrial", "Century Gothic", sans-serif;
    position: relative;
  }
  .side-label {
    position: absolute;
    left: 250px;
    font-size: 16px;
    letter-spacing: 3px;
    color: var(--grey-text);
    font-weight: bold;
  }
  .side-label--back { top: 20px; }
  .side-label--front { top: 500px; }

  .card {
    position: absolute;
    left: 250px;
    width: 700px;
    height: 420px;
    overflow: hidden;
    box-shadow: 0 8px 24px rgba(0,0,0,0.18);
  }

  /* Back */
  .card--back {
    top: 50px;
    background: radial-gradient(ellipse at 30% 45%, var(--navy) 0%, var(--navy-deep) 75%);
  }
  .card--back .brand-dot {
    position: absolute;
    left: 60px; top: 70px;
    width: 270px; height: 270px;
    border-radius: 50%;
    background: var(--blue);
  }
  .card--back .brand-name {
    position: absolute;
    left: 370px; top: 55px;
    font-size: 50px;
    line-height: 1.05;
    color: var(--green);
  }
  .services {
    position: absolute;
    left: 370px; top: 215px;
    list-style: none;
    font-size: 21px;
    line-height: 1.3;
    color: var(--blue-light);
  }
  .tagline {
    position: absolute;
    left: 370px; top: 345px;
    font-size: 21px;
    color: var(--blue);
  }

  /* Front */
  .card--front { top: 530px; background: var(--paper); }
  .holder-name {
    position: absolute;
    left: 32px; top: 40px;
    font-size: 26px;
    color: var(--grey-text);
  }
  .holder-name .given { color: var(--green); }
  .holder-title {
    position: absolute;
    left: 32px; top: 76px;
    font-size: 14px;
    letter-spacing: 2px;
    color: var(--grey-text);
  }
  .rule {
    position: absolute;
    left: 32px; top: 100px;
    width: 640px; height: 2px;
    background: linear-gradient(90deg, rgba(124,201,54,0.2), var(--green));
  }
  .contact {
    position: absolute;
    right: 30px;
    display: flex;
    align-items: center;
    gap: 10px;
    font-size: 16px;
    color: var(--grey-text);
  }
  .contact--phone { top: 115px; }
  .contact--email { top: 148px; }
  .contact svg { width: 16px; height: 16px; fill: var(--green); }
  .band {
    position: absolute;
    left: 0; top: 188px;
    width: 700px; height: 165px;
    background: radial-gradient(ellipse at 40% 50%, var(--navy) 0%, var(--navy-deep) 80%);
  }
  .band .brand-dot {
    position: absolute;
    left: 200px; top: 22px;
    width: 120px; height: 120px;
    border-radius: 50%;
    background: var(--blue);
  }
  .band .brand-name {
    position: absolute;
    left: 345px; top: 40px;
    font-size: 38px;
    line-height: 1.05;
    color: var(--green);
  }
  .website {
    position: absolute;
    left: 0; top: 375px;
    width: 700px;
    text-align: center;
    font-size: 15px;
    letter-spacing: 3px;
    color: var(--grey-text);
  }
</style>
</head>
<body>
  <div class="side-label side-label--back">BACK</div>
  <section class="card card--back">
    <div class="brand-dot"></div>
    <div class="brand-name">The Velvet<br>Lattice</div>
    <ol class="services">
      <li>1. 3d Design and Modelling</li>
      <li>2. 3d Animation</li>
      <li>3. 3D Printing</li>
    </ol>
    <p class="tagline">make your ideas real</p>
  </section>

  <div class="side-label side-label--front">FRONT</div>
  <section class="card card--front">
    <h1 class="holder-name"><span class="given">Raghavan</span>Kulkarni</h1>
    <p class="holder-title">Founder Director</p>
    <div class="rule"></div>
    <p class="contact contact--phone">(65)91827345
      <svg viewBox="0 0 24 24" aria-hidden="true"><path d="M6.6 10.8a15.1 15.1 0 0 0 6.6 6.6l2.2-2.2a1 1 0 0 1 1-.25 11.4 11.4 0 0 0 3.6.57 1 1 0 0 1 1 1V20a1 1 0 0 1-1 1A17 17 0 0 1 3 4a1 1 0 0 1 1-1h3.5a1 1 0 0 1 1 1c0 1.25.2 2.45.57 3.57a1 1 0 0 1-.25 1z"/></svg>
    </p>
    <p class="contact contact--email">raghavan@velvetlattice.com.sg
      <svg viewBox="0 0 24 24" aria-hidden="true"><path d="M3 5h18v14H3z M3 5l9 7 9-7" /></svg>
    </p>
    <div class="band">
      <div class="brand-dot"></div>
      <div class="brand-name">The Velvet<br>Lattice</div>
    </div>
    <p class="website">www.velvetlattice.com.sg</p>
  </section>
</body>
</html>
```